Orvessa Develoipment and Management Corp Web Design Project

Website... Based on logo. Update forthcoming....
Updates

Reason: Extended to include recently completed logo design.

Target Market(s)

Financiers, investors, public officials, and landowners.

Industry/Entity Type

Management

Requirements
Should not have
• No palm trees, mayan ruins, or other Caribbean references.

```html
<!DOCTYPE html>
<html lang="en">
<head>
<meta charset="utf-8">
<title>Orvessa Develoipment and Management Corp</title>
<link rel="stylesheet" href="https://fonts.googleapis.com/css2?family=Open+Sans:wght@400;600&display=swap">
<style>
  :root {
    --bg: #25282f;
    --rule: #3b3f47;
    --text: #e2e2e2;
    --muted: #8b8e94;
    --accent: #a6c23b;
    --social: #5e8f3a;
    --photo-sky: #8aa3bd;
    --photo-city: #4d5c6c;
    --photo-trees: #2f4a27;
  }
  * { box-sizing: border-box; margin: 0; padding: 0; }
  html, body { width: 1200px; height: 1000px; overflow: hidden; }
  body {
    background: var(--bg);
    color: var(--text);
    font-family: "Open Sans", Arial, sans-serif;
    font-size: 20.5px;
    line-height: 28.4px;
  }
  .page { position: relative; width: 1200px; height: 1000px; }
  .site-header {
    position: absolute; left: 160px; top: 40px; width: 872px; height: 108px;
    border-bottom: 3px solid var(--rule);
  }
  .brand-mark { position: absolute; left: 14px; top: 20px; width: 64px; height: 64px; background: var(--muted); }
  .brand-name {
    position: absolute; left: 103px; top: 2px;
    color: var(--accent); font-size: 56px; font-weight: 600; line-height: 66px; letter-spacing: 1px;
    white-space: nowrap;
  }
  .brand-tagline {
    position: absolute; left: 105px; top: 68px;
    color: var(--muted); font-size: 15.5px; line-height: 20px; white-space: nowrap;
  }
  .main-nav { position: absolute; right: 3px; top: 38px; display: flex; gap: 34px; }
  .main-nav a { color: var(--muted); text-decoration: none; font-size: 21px; line-height: 28px; }
  .main-nav a.is-current { color: var(--accent); }
  .content p { position: absolute; white-space: nowrap; }
  .content em { font-style: normal; color: var(--accent); }
  .intro-1 { left: 160px; top: 171px; }
  .intro-2 { left: 160px; top: 284px; }
  .feature-text { left: 158px; top: 397px; }
  .outro { left: 158px; top: 794px; }
  .feature-photo {
    position: absolute; left: 595px; top: 401px; width: 449px; height: 369px;
    background: linear-gradient(180deg, var(--photo-sky) 0%, #b9c3cc 40%, var(--photo-city) 70%, var(--photo-trees) 100%);
    box-shadow: 0 4px 10px rgba(0,0,0,.35);
  }
  .site-footer {
    position: absolute; left: 158px; top: 877px; width: 872px;
    border-top: 3px solid var(--rule); padding-top: 14px;
  }
  .contact-line { display: flex; align-items: center; height: 28px; font-size: 20.5px; white-space: nowrap; }
  .contact-line svg { width: 18px; height: 18px; margin: 0 10px 0 2px; fill: var(--accent); }
  .contact-label { color: var(--accent); margin-right: 9px; }
  .social { position: absolute; right: 0; top: 22px; display: flex; gap: 18px; }
  .social a { display: flex; align-items: center; gap: 8px; color: var(--social); text-decoration: none; font-weight: 600; font-size: 20px; }
  .social .dot { width: 14px; height: 14px; background: var(--social); }
</style>
</head>
<body>
<div class="page">
  <header class="site-header">
    <div class="brand">
      <span class="brand-mark" aria-hidden="true"></span>
      <span class="brand-name">ORVESSA</span>
      <span class="brand-tagline">Develoipment and Management Corp</span>
    </div>
    <nav class="main-nav">
      <a href="#" class="is-current">Home</a>
      <a href="#">News</a>
      <a href="#">About Us</a>
      <a href="#">Contact Us</a>
    </nav>
  </header>

  <main class="content">
    <p class="intro-1">Lorem ipsum dolor sit amet, consectetur adipiscing elit. Maecenas pellentesque dolor nisi,<br>mattis maximus tortor fringilla eu. Maecenas molestie vitae quam ut <em>placerat</em>. Nullam vitae<br>blandit <em>sapien</em>. Aenean at scelerisque libero, quis facilisis diam.</p>
    <p class="intro-2">Ut ac arcu diam. Ut ac turpis enim. Duis at ligula <em>vitae</em> diam pharetra mattis. Aenean ut<br>magna orci. Suspendisse malesuada mattis accumsan. Aliquam ultrices nisl id augue<br>pretium, nec accumsan mauris fringilla.</p>
    <p class="feature-text"><em>Lorem</em> ipsum dolor sit amet, consectetur<br>adipiscing elit. Morbi sollicitudin blandit<br>nulla id dictum. Sed non porttitor ipsum.<br>Pellentesque id semper nibh. Nam eros<br>lacus, elementum a <em>efficitur</em> luctus, dictum<br>et mauris. Sed eget justo quis eros<br>tincidunt mollis eu in dui. Proin at ipsum<br><em>sapien</em>. Cras sit amet lacus eget nisi<br>condimentum fringilla sit amet <em>eget</em> lorem.<br>Mauris posuere dolor ac ullamcorper<br>elementum. <em>Mauris</em> at ante pellentesque,<br>pharetra turpis nec, lacinia enim.<br>Etiam dui enim, eleifend eget nibh ornare.</p>
    <div class="feature-photo" role="img" aria-label="Photo of a glass high-rise tower and city skyline behind trees under a cloudy sky"></div>
    <p class="outro">Pellentesque massa erat, suscipit ut accumsan <em>eget</em>, lacinia non velit. Pellentesque gravida<br><em>dui</em> ac ultricies ullamcorper.</p>
  </main>

  <footer class="site-footer">
    <div class="contact-line">
      <svg viewBox="0 0 24 24" aria-hidden="true"><path d="M6.6 10.8a15 15 0 0 0 6.6 6.6l2.2-2.2a1 1 0 0 1 1-.25 11.4 11.4 0 0 0 3.6.57 1 1 0 0 1 1 1V20a1 1 0 0 1-1 1A17 17 0 0 1 3 4a1 1 0 0 1 1-1h3.5a1 1 0 0 1 1 1c0 1.25.2 2.45.57 3.57a1 1 0 0 1-.25 1z"/></svg>
      <span class="contact-label">Tel:</span><span>555 0198362</span>
    </div>
    <div class="contact-line">
      <svg viewBox="0 0 24 24" aria-hidden="true"><path d="M2 5h20v2l-10 6L2 7z"/><path d="M2 9l10 6 10-6v10H2z"/></svg>
      <span class="contact-label">E-Mail:</span><span>hello@orvessamail.com</span>
    </div>
    <div class="social">
      <a href="#"><span class="dot"></span>Chirpline</a>
      <a href="#"><span class="dot"></span>Friendwall</a>
    </div>
  </footer>
</div>
</body>
</html>
```